Boutique furnished offices with "high end" childcare centre require Wordpress website template

Project Overview: We require a wordpress design for a new company based in South Perth Western Australia, "The Harbour 19 Collective" which provide centres where parents can utilise childcare whilst hiring furnished offices and co-working spaces. We also provide onsite beauty, hair, gymnasium and park & ride facilities into the CBD which can all be booked online through our website (plugins required to be used to book through https://quickslotter.example/). We are a one stop shop where you can drop your children at childcare, skip the traffic and ride the ferry into the CBD. Or simply have your children cared for whilst you work out of our furnished office facilities.
The website design should be classy, modern, gender neutral and corporate (not too children focused/playful).

Look And Feel: clean, classy, modern site which is easy to navigate and book services online. It must also be gender neutral and corporate (not children focused/playful).
A typical childcare centre feel - we aren’t going for "jellybeans and teddybears" we are looking for a classy, corporate and sophisticated feel.

(LOGO currently being finalised but is charcoal grey on a white back ground and attached below - but will all be in lower case not capitals)

Target Market(s)

Target market is working parents, predominantly corporate or consultants running their own businesses.

Industry/Entity Type

Boutique

Number of Pages Required

2 page

Requirements
Must have
• The following would be required of the winning submission:
• • Clean, classy, modern site which is easy to navigate and book services online. It must also be gender neutral and corporate (not children focused/playful).
• • Require simplistic homepage with Menu of list of services, and template for individual pages for each of the services offered (child care, furnished offices, park & ride, hair/ beauty, gymnasium)
• • Necessary customization/plugins to allow online bookings to be placed https://quickslotter.example/
• • Well placed plugin/customization to link and also allow "share it" type links to major social networks (linkedin, facebook, twitter, google+, etc.).
• • All design components should be optimized for indexing on major search engines
• • Wordpress theme that is supported in Chrome, IE 8+, firefox, and safari
Nice to have
• Included below is a list of sites that we like from a simplicity and clean look and feel.
• http://www.lumenfold.example.au/
• http://www.wanderthegardenpath.example.uk/
• http://www.velopiccolo.example/
• http://www.qvframe.example.au/
• http://madebymarten.example/

```html
<!DOCTYPE html>
<html lang="en">
<head>
<meta charset="utf-8">
<title>The Harbour 19 Collective</title>
<link href="https://fonts.googleapis.com/css2?family=Figtree:wght@400;500;600;700&display=swap" rel="stylesheet">
<style>
:root{
  --ink:#555658;
  --ink-soft:#6d6e70;
  --muted:#9a9b9d;
  --rule:#cfd0d2;
  --panel:#5d5e60;
  --white:#ffffff;
  --photo-warm:#efe3cf;
  --photo-grey:#9a9a9a;
}
*{box-sizing:border-box;margin:0;padding:0}
html,body{width:706px;height:1200px;overflow:hidden;background:var(--white)}
body{position:relative;font-family:"Figtree",Arial,sans-serif;color:var(--ink)}
.abs{position:absolute}
a{color:inherit;text-decoration:none}

.brand{left:0;width:706px;top:30px;text-align:center;font-size:15px;font-weight:600;letter-spacing:.5px;color:var(--ink)}
.brand-mark{display:inline-block;width:10px;height:10px;border-radius:50%;border:1.5px solid var(--ink);margin-right:7px;vertical-align:0}

.main-nav{left:58px;top:84px;display:flex;font-size:6.5px;letter-spacing:.4px;text-transform:uppercase;color:var(--ink)}
.main-nav li{list-style:none;display:flex;align-items:center}
.main-nav .sep{color:var(--muted);margin:0 14px}
.booking{left:539px;top:69px;width:108px;height:36px;background:var(--panel);color:var(--white);font-size:6.5px;letter-spacing:.4px;display:flex;align-items:center;justify-content:space-between;padding:0 13px}

.hero-photo{left:58px;top:108px;width:294px;height:262px;background:linear-gradient(135deg,#fafafa 0%,var(--photo-warm) 50%,#f6f1ea 100%)}
.hero-copy{left:413px;top:164px;width:234px}
.hero-copy h1{font-size:17px;font-weight:700;color:var(--ink);line-height:1.2;white-space:nowrap}
.hero-copy p{margin-top:12px;font-size:8px;line-height:1.9;color:var(--ink-soft);width:226px}
.btn-outline{display:inline-flex;align-items:center;gap:14px;margin-top:12px;border:1px solid var(--ink-soft);padding:5px 8px 5px 9px;font-size:7px}
.dots{left:612px;top:298px;display:flex;gap:3px}
.dots span{width:4px;height:4px;border-radius:50%;background:#dadbdc}
.dots span:first-child{background:#a9aaac}

.mission{left:346px;top:318px;width:301px;height:194px;background:var(--panel);color:var(--white);padding:36px 34px 0 44px}
.mission h2{font-size:24px;font-weight:700}
.mission p{margin-top:14px;font-size:7px;line-height:2.1}
.mission .link{margin-top:12px;text-align:right;font-size:7.5px}

.about{left:61px;top:400px;width:230px}
.about h2{font-size:27px;font-weight:700;color:var(--ink)}
.underline{width:34px;height:1px;background:var(--ink-soft);margin-top:14px}
.about p{margin-top:14px;font-size:6.5px;line-height:2.2;color:var(--ink-soft)}

.service-nav{left:59px;top:578px}
.service-nav li{list-style:none;display:flex;align-items:center;height:16px;font-size:7.5px;color:var(--ink)}
.service-nav .dot{width:4.5px;height:4.5px;border-radius:50%;background:#b8b9bb}
.service-nav .active .dot{background:var(--ink)}
.service-nav .dash{width:18px;height:1px;background:var(--ink);margin:0 8px 0 9px}

.service-photo{left:195px;top:577px;width:162px;height:193px;background:linear-gradient(160deg,#6d6d6d 0%,var(--photo-grey) 45%,#d8d8d8 100%)}
.service-copy{left:409px;top:588px;width:210px}
.service-copy h2{font-size:25px;font-weight:700}
.service-copy p{margin-top:14px;font-size:6.5px;line-height:2.2;color:var(--ink-soft)}
.service-copy .link{margin-top:12px;text-align:right;font-size:7.5px;color:var(--ink)}

.tips-title{left:0;width:706px;top:823px;text-align:center}
.tips-title h2{font-size:27px;font-weight:700}
.tips-title .underline{margin:12px auto 0}
.tip{top:892px;width:177px}
.tip .thumb{height:74px}
.tip h3{margin-top:12px;font-size:8px;font-weight:600;color:var(--ink)}
.tip .more{margin-top:7px;font-size:6px;color:var(--muted)}

.footer-rule{left:58px;top:1042px;width:589px;height:1px;background:#e2e3e4}
.fcol{top:1066px}
.fcol h4{font-size:8px;font-weight:600;color:var(--ink)}
.fcol p,.fcol li{font-size:6px;color:var(--muted);list-style:none}
.fcol p{margin-top:8px}
.signup{margin-top:9px;width:178px;height:20px;border:1px solid var(--rule);display:flex;align-items:center;justify-content:space-between;padding:0 7px;font-size:6px;color:var(--muted)}
.contact li{display:flex;align-items:center;gap:6px;margin-top:6px}
.social{display:flex;gap:11px;margin-top:10px}
.social span{width:10px;height:10px;border-radius:50%;background:#b3b4b6}

.bottom-nav{left:60px;top:1155px;display:flex;font-size:6px;color:var(--muted)}
.bottom-nav .sep{margin:0 8px}
.copyright{left:497px;top:1155px;font-size:6px;color:var(--muted)}
</style>
</head>
<body>

<header>
  <div class="abs brand"><span class="brand-mark"></span>The Harbour 19 Collective</div>
  <ul class="abs main-nav">
    <li>Home</li><li class="sep">-</li>
    <li>About</li><li class="sep">-</li>
    <li>Services</li><li class="sep">-</li>
    <li>Tips &amp; Tricks</li><li class="sep">-</li>
    <li>Blog</li><li class="sep">-</li>
    <li>Testimonials</li><li class="sep">-</li>
    <li>Contact Us</li>
  </ul>
  <a class="abs booking" href="#">ONLINE BOOKING
    <svg width="6" height="4" viewBox="0 0 6 4"><path d="M.5.5 3 3 5.5.5" fill="none" stroke="#fff" stroke-width="1"/></svg>
  </a>
</header>

<section class="hero">
  <div class="abs hero-photo" role="img" aria-label="Portrait of a woman with long curly blonde hair on a white background"></div>
  <div class="abs hero-copy">
    <h1>The Harbour 19 Collective</h1>
    <p>Services we provide are child care, furnished offices, park &amp; ride, hair/ beauty, gymnasium.</p>
    <a class="btn-outline" href="#">Read more
      <svg width="9" height="6" viewBox="0 0 9 6"><path d="M0 3h8M5.5.5 8 3 5.5 5.5" fill="none" stroke="#555658" stroke-width=".9"/></svg>
    </a>
  </div>
  <div class="abs dots"><span></span><span></span><span></span><span></span></div>
</section>

<section class="abs mission">
  <h2>Our Mission</h2>
  <p>Lorem Ipsum is simply dummy text of the printing and typesetting industry. Lorem Ipsum has been the industry's standard dummy text ever since the 1500s, when an unknown printer took a galley of type and scrambled it to make a type specimen book.</p>
  <div class="link">Contact Us
    <svg width="9" height="6" viewBox="0 0 9 6"><path d="M0 3h8M5.5.5 8 3 5.5 5.5" fill="none" stroke="#fff" stroke-width=".9"/></svg>
  </div>
</section>

<section class="abs about">
  <h2>Who we are</h2>
  <div class="underline"></div>
  <p>Lorem Ipsum is simply dummy text of the printing and typesetting industry. Lorem Ipsum has been the industry's standard dummy text ever since the 1500s, when an unknown printer took a galley of type and scrambled it to make a type specimen...</p>
</section>

<section class="services">
  <ul class="abs service-nav">
    <li class="active"><span class="dot"></span><span class="dash"></span>Child care</li>
    <li><span class="dot"></span></li>
    <li><span class="dot"></span></li>
    <li><span class="dot"></span></li>
    <li><span class="dot"></span></li>
  </ul>
  <div class="abs service-photo" role="img" aria-label="Black and white photo of a mother holding her baby"></div>
  <div class="abs service-copy">
    <h2>Child care</h2>
    <div class="underline"></div>
    <p>Lorem Ipsum is simply dummy text of the printing and typesetting industry. Lorem Ipsum has been the industry's standard dummy text ever since the 1500s, when an unknown printer took a galley of type and scrambled it to make a type specimen text ever since the 1500s, when an unknown printer took a galley of type and scrambled it to make a type specimen...</p>
    <div class="link">Read more
      <svg width="9" height="6" viewBox="0 0 9 6"><path d="M0 3h8M5.5.5 8 3 5.5 5.5" fill="none" stroke="#555658" stroke-width=".9"/></svg>
    </div>
  </div>
</section>

<section class="tips">
  <div class="abs tips-title"><h2>Tips &amp; Tricks</h2><div class="underline"></div></div>
  <article class="abs tip" style="left:58px">
    <div class="thumb" role="img" aria-label="Carers playing with a baby in a bright room" style="background:linear-gradient(120deg,#e9efe6,#d9b9a3 55%,#7d93b0)"></div>
    <h3>Lorem Ipsum is simply dummy</h3>
    <div class="more">Click here for more info →</div>
  </article>
  <article class="abs tip" style="left:264px">
    <div class="thumb" role="img" aria-label="Group fitness class on exercise bikes" style="background:linear-gradient(120deg,#8fa2b6,#c9a89a 50%,#3c3f48)"></div>
    <h3>Lorem Ipsum is simply dummy</h3>
    <div class="more">Click here for more info →</div>
  </article>
  <article class="abs tip" style="left:470px">
    <div class="thumb" role="img" aria-label="Woman with styled hair beside a bouquet of flowers" style="background:linear-gradient(120deg,#e6c4a8,#caa08a 50%,#a5748a)"></div>
    <h3>Lorem Ipsum is simply dummy</h3>
    <div class="more">Click here for more info →</div>
  </article>
</section>

<footer>
  <div class="abs footer-rule"></div>
  <div class="abs fcol" style="left:58px">
    <h4>Newsletter signup</h4>
    <p>Get our latest updates through your email id</p>
    <div class="signup">Enter your email id
      <svg width="9" height="6" viewBox="0 0 9 6"><path d="M0 3h8M5.5.5 8 3 5.5 5.5" fill="none" stroke="#9a9b9d" stroke-width=".9"/></svg>
    </div>
  </div>
  <div class="abs fcol contact" style="left:297px">
    <h4>Contact Info</h4>
    <ul>
      <li style="margin-top:9px">27 Ferry Road, Harbourside, Country name : 604127</li>
      <li><svg width="7" height="7" viewBox="0 0 10 10"><path d="M2 1h2l1 2.5-1.3.8a6 6 0 0 0 2 2l.8-1.3L9 6v2a1 1 0 0 1-1 1A8 8 0 0 1 1 2a1 1 0 0 1 1-1z" fill="#9a9b9d"/></svg>( 985 ) 555 - 0142</li>
      <li><svg width="7" height="6" viewBox="0 0 10 8"><rect x=".5" y=".5" width="9" height="7" fill="none" stroke="#9a9b9d"/><path d="M.5.5 5 4.5 9.5.5" fill="none" stroke="#9a9b9d"/></svg>info@harbour19collective.example</li>
    </ul>
  </div>
  <div class="abs fcol" style="left:520px">
    <h4>Follow Us</h4>
    <p>Connect with our social network</p>
    <div class="social" aria-label="Social network links"><span></span><span></span><span></span><span></span></div>
  </div>
  <div class="abs bottom-nav">
    <span>Home</span><span class="sep">-</span><span>About</span><span class="sep">-</span><span>Services</span><span class="sep">-</span><span>Tips &amp; Tricks</span><span class="sep">-</span><span>Blog</span><span class="sep">-</span><span>Testimonials</span><span class="sep">-</span><span>Contact Us</span>
  </div>
  <div class="abs copyright">© 2016. The Harbour 19 Collective. All rights reserved.</div>
</footer>

</body>
</html>
```